Business Card Design Project for Electrical Company

We need a business card designed for a new Electrical Company called Dorvel Electrical Solutions, i dont mind if only Dorvel Electrical is used. We are a domestic and commercial Electrical Company that provides a range of Electrical Services. Our Company colours are Fluro Yellow and Black with the Lightning bolt picture attached.I have attached a card that has been made i think it is rather basic and am looking for something more. the font of Dorvel Electrical has been used on our car graphics as well as the lightning bolt. i want to keep them the same so we can brand our business. Some things we want on the front of the card are Dorvel Electrical Solutions, Owen Platt, 0438516274, admin@dorvelelectrical.example, Lic No 58342, Servicing CQ Region. But we want Owens name seperate to the phone number as its the phone number for the office, owen wont be answering the phone so we are thinking we dont want to give that impression. What do you think? with all that if you have complete different font designs please submit what you think would work best. keeping in mind our company name and details as well as coulors.

Industry/Entity Type

Business

```html
<!DOCTYPE html>
<html lang="en">
<head>
<meta charset="utf-8">
<title>Dorvel Electrical Solutions – Business Card</title>
<link rel="stylesheet" href="https://fonts.googleapis.com/css2?family=Arimo:wght@400;700&family=Cinzel:wght@400&family=Gentium+Book+Plus&display=swap">
<style>
  :root {
    --bg: #2a2a2a;
    --card-black: #050505;
    --card-white: #ffffff;
    --fluro: #d4e12b;
    --ink: #151515;
    --paper-text: #ffffff;
  }
  * { margin: 0; padding: 0; box-sizing: border-box; }
  html, body { width: 1200px; height: 942px; overflow: hidden; }
  body {
    background: var(--bg);
    position: relative;
    font-family: "Arimo", Arial, sans-serif;
  }
  .card {
    position: absolute;
    top: 316px;
    width: 540px;
    height: 310px;
    overflow: hidden;
  }
  .card--front { left: 40px; background: var(--card-white); }
  .card--back { left: 620px; background: var(--card-black); }

  .bolt-art {
    position: absolute;
    background: linear-gradient(110deg, rgba(60,60,60,.55), rgba(200,200,200,.15) 70%, transparent);
  }
  .card--front .bolt-art { left: 0; top: 70px; width: 230px; height: 190px; }
  .card--back .bolt-art {
    left: 0; top: 110px; width: 140px; height: 110px;
    background: linear-gradient(110deg, rgba(230,230,230,.3), rgba(120,120,120,.08) 70%, transparent);
  }

  .brand {
    position: absolute;
    display: flex;
    align-items: center;
    gap: 10px;
    line-height: 1.15;
  }
  .brand__dot { border-radius: 50%; background: var(--fluro); flex: none; }
  .card--front .brand {
    left: 140px; top: 140px;
    font-size: 32px; font-weight: 700; color: var(--ink);
    width: 380px;
  }
  .card--front .brand__dot { width: 24px; height: 24px; }
  .card--back .brand {
    left: 22px; top: 90px;
    font-size: 12px; font-weight: 400; color: var(--paper-text);
    white-space: nowrap;
  }

  .name {
    position: absolute;
    right: 34px; top: 52px;
    font-family: "Gentium Book Plus", Georgia, serif;
    font-weight: 400;
    font-size: 60px;
    color: var(--paper-text);
    white-space: nowrap;
  }
  .role {
    position: absolute;
    left: 200px; right: 20px; top: 134px;
    text-align: center;
    font-size: 22px;
    color: var(--paper-text);
  }
  .licence {
    position: absolute;
    left: 170px; right: 10px; top: 176px;
    text-align: center;
    font-family: "Cinzel", "Times New Roman", serif;
    font-size: 17px;
    color: var(--paper-text);
  }
  .contact-band {
    position: absolute;
    left: 0; right: 0; top: 230px; height: 58px;
    background: var(--card-white);
  }
  .contact-band__rule {
    position: absolute;
    left: 0; right: 0; top: 24px; height: 6px;
    background: var(--fluro);
  }
  .contact {
    position: absolute;
    font-size: 11px;
    color: var(--ink);
  }
  .contact strong { font-size: 14px; font-weight: 400; }
  .contact--phone { right: 18px; top: 4px; }
  .contact--email { left: 18px; top: 36px; }
</style>
</head>
<body>
  <section class="card card--front" aria-label="Card front">
    <div class="bolt-art" role="img" aria-label="Lightning bolt branches spreading from the left edge"></div>
    <div class="brand"><span class="brand__dot"></span><span>Dorvel Electrical Solutions</span></div>
  </section>

  <section class="card card--back" aria-label="Card back">
    <div class="bolt-art" role="img" aria-label="Lightning bolt branches behind the company name"></div>
    <div class="brand"><span>Dorvel Electrical Solutions</span></div>
    <h1 class="name">Owen Platt</h1>
    <p class="role">Licensed Electrician</p>
    <p class="licence">Lic No. 58342/Servicing CQ Region.</p>
    <div class="contact-band">
      <div class="contact-band__rule"></div>
      <p class="contact contact--phone">Phone: <strong>0438516274</strong></p>
      <p class="contact contact--email">Email: <strong>admin@dorvelelectrical.example</strong></p>
    </div>
  </section>
</body>
</html>
```